New Patient Dental Flyer for Tamblin Ridge Dental

I am looking for flyer for a dental practice that brings in new patients and follows QPRS guidelines and dimensions (5.5" X 8.5"). I have a logo that I would like used.
Content: Name: TAMBLIN RIDGE DENTAL
4318 West Tamblin Road, Suite 260
Salt Lake City, UT 84372
Phone: 801-555-0143
Fax: 801-555-0198

Free Whitening Club
New Patient Cleaning & Exam
Free Clearovo Consultation
$39 Emergency Exam & X-rays
I would like the Flyer to include a small easy to read map to our location. I would like the colors to match the logo if possible.

Target Market(s)

New Patients and Patients without insurance. Ages 18-65

Industry/Entity Type

Dental Clinic

Font styles to use
Serif
Sans Serif

Colors

Designer to choose colors to be used in the design.

Requirements
Must have
• Logo and clear map to location that is easily to follow.
Nice to have
• Promotional ideas not included but designer recommendations

```html
<!DOCTYPE html>
<html lang="en">
<head>
<meta charset="utf-8">
<title>Tamblin Ridge Dental – New Patient Postcard</title>
<link href="https://fonts.googleapis.com/css2?family=Raleway:wght@400;500&family=Source+Sans+3:wght@400;600;700&family=Arimo:wght@400;700&display=swap" rel="stylesheet">
<style>
  :root {
    --slate: #7a8fae;
    --slate-dark: #6f7fa0;
    --navy: #537590;
    --green: #6cb87f;
    --green-text: #5fb27a;
    --lime: #d8e59a;
    --ink: #3e4348;
    --grey: #5a5f66;
    --paper: #ffffff;
    --bg: #eceff2;
  }
  * { box-sizing: border-box; margin: 0; padding: 0; }
  html, body { width: 1002px; height: 1200px; overflow: hidden; background: var(--bg); }
  body { font-family: "Source Sans 3", Arial, sans-serif; color: var(--ink); position: relative; }

  .card-slot { position: absolute; left: 61px; width: 880px; height: 570px; }
  .card-slot.front { top: 20px; }
  .card-slot.back { top: 610px; }
  .card {
    position: absolute; left: 0; top: 0; width: 850px; height: 550px;
    transform: scale(1.0353); transform-origin: 0 0;
    background: var(--paper); overflow: hidden;
    box-shadow: 0 2px 8px rgba(0,0,0,.18);
  }
  .card-art { position: absolute; inset: 0; }
  .abs { position: absolute; }

  .brand { display: flex; align-items: center; gap: 12px; }
  .brand-dot { width: 40px; height: 40px; border-radius: 50%; background: var(--slate-dark); }
  .brand-name { font-family: "Source Sans 3", sans-serif; font-weight: 400; font-size: 34px; color: var(--slate-dark); white-space: nowrap; }

  /* Front */
  .headline-band { left: 440px; top: 122px; width: 410px; height: 116px; background: var(--slate); color: #fff; text-align: center; }
  .headline-band .kicker { font-size: 13px; font-weight: 600; margin-top: 8px; letter-spacing: .2px; }
  .headline-band h1 { font-family: "Raleway", sans-serif; font-weight: 400; font-size: 36px; line-height: 42px; letter-spacing: .5px; margin-top: 2px; }
  .perks { left: 466px; top: 259px; width: 380px; display: grid; grid-template-columns: 189px 191px; row-gap: 8px; font-size: 12.5px; color: var(--grey); }
  .perks li { list-style: none; display: flex; align-items: center; gap: 4px; white-space: nowrap; }
  .tick { width: 12px; height: 12px; flex: none; }
  .insurance { font-family: "Raleway", sans-serif; color: var(--green-text); font-size: 15px; }
  .front .insurance { left: 440px; width: 410px; top: 312px; text-align: center; }

  .offer { top: 355px; width: 178px; height: 116px; border-radius: 6px; overflow: hidden; background: var(--green); color: #fff; text-align: center; box-shadow: 0 2px 4px rgba(0,0,0,.18); }
  .offer .tag { background: #f2f2f2; color: var(--grey); font-size: 11px; font-weight: 700; height: 21px; line-height: 22px; }
  .offer .lead { font-size: 13px; font-weight: 600; margin-top: 3px; }
  .offer .big { font-size: 30px; font-weight: 600; line-height: 32px; }
  .offer .big small { font-size: 21px; }
  .offer .fine { font-size: 10.5px; line-height: 13px; }
  .offer .body { font-size: 13px; line-height: 15px; }

  .cta { left: 0; width: 850px; top: 496px; text-align: center; color: #fff; font-family: "Raleway", sans-serif; font-size: 20px; display: flex; justify-content: center; align-items: center; gap: 12px; }
  .cta .phone-num { font-family: "Source Sans 3", sans-serif; font-weight: 700; font-size: 22px; letter-spacing: .5px; }
  .cta svg { width: 22px; height: 22px; }

  /* Back */
  .address-band { left: 0; top: 107px; width: 425px; height: 49px; background: var(--slate); color: #fff; font-size: 17px; display: flex; align-items: center; padding-left: 22px; gap: 8px; }
  .map-area { left: 0; top: 156px; width: 448px; height: 114px; background: linear-gradient(135deg, #eceae6, #dcdcd8); }
  .directions { left: 30px; top: 294px; width: 360px; text-align: center; font-size: 13px; line-height: 16px; color: var(--grey); }
  .hours { left: 20px; top: 333px; width: 380px; text-align: center; font-family: "Raleway", sans-serif; font-weight: 500; font-size: 17px; color: var(--navy); }
  .back .insurance { left: 20px; top: 356px; width: 380px; text-align: center; font-size: 17px; }
  .badge { left: 395px; top: 327px; width: 136px; height: 136px; border-radius: 50%; background: var(--green); border: 4px solid #fff; box-shadow: 0 1px 4px rgba(0,0,0,.2); color: #fff; font-size: 14.5px; line-height: 20px; text-align: center; display: flex; align-items: center; justify-content: center; }
  .return-address { left: 489px; top: 33px; font-size: 13.5px; line-height: 17.6px; color: var(--ink); }
  .indicia { left: 730px; top: 25px; width: 97px; height: 97px; border: 1px solid #555; font-family: "Arimo", Arial, sans-serif; font-size: 12.5px; line-height: 15.5px; text-align: center; padding-top: 8px; color: #111; }
  .mail-block { left: 546px; top: 199px; width: 281px; height: 112px; border: 1px solid #555; font-family: "Arimo", Arial, sans-serif; color: #111; }
  .mail-block .route { position: absolute; right: 22px; top: 14px; font-size: 12.5px; }
  .mail-block .recipient { position: absolute; left: 20px; top: 55px; font-size: 16px; line-height: 19px; }
</style>
</head>
<body>

<!-- Front of postcard -->
<div class="card-slot front">
  <section class="card front">
    <svg class="card-art" viewBox="0 0 850 550" aria-hidden="false">
      <defs>
        <linearGradient id="photoTone" x1="0" y1="0" x2="1" y2="1">
          <stop offset="0" stop-color="#2f4a32"/>
          <stop offset=".6" stop-color="#3d5a3c"/>
          <stop offset="1" stop-color="#4d6178"/>
        </linearGradient>
      </defs>
      <path role="img" aria-label="Photo of a smiling young family of three in front of an ivy wall" d="M0 0 H322 C385 115 425 260 434 480 H0 Z" fill="url(#photoTone)"/>
      <path d="M332 -6 C398 110 436 250 442 480" fill="none" stroke="var(--slate)" stroke-width="18"/>
      <path d="M352 -6 C420 118 452 260 452 380" fill="none" stroke="var(--lime)" stroke-width="6"/>
      <path d="M0 452 C260 478 560 452 850 392 V420 C560 476 260 492 0 470 Z" fill="var(--lime)"/>
      <path d="M0 462 C260 486 560 462 850 408 V550 H0 Z" fill="var(--navy)"/>
    </svg>

    <div class="abs brand" style="left:468px; top:44px;">
      <span class="brand-dot"></span>
      <span class="brand-name">Tamblin Ridge Dental</span>
    </div>

    <div class="abs headline-band">
      <p class="kicker">YEAR LONG</p>
      <h1>GRAND REOPENING<br>CELEBRATION</h1>
    </div>

    <ul class="abs perks">
      <li><svg class="tick" viewBox="0 0 12 12"><circle cx="6" cy="6" r="5" fill="none" stroke="var(--slate)" stroke-width="1.2"/><path d="M3.5 6.2 L5.3 8 L8.6 4.3" fill="none" stroke="var(--slate)" stroke-width="1.2"/></svg>Free Whitening Club</li>
      <li><svg class="tick" viewBox="0 0 12 12"><circle cx="6" cy="6" r="5" fill="none" stroke="var(--slate)" stroke-width="1.2"/><path d="M3.5 6.2 L5.3 8 L8.6 4.3" fill="none" stroke="var(--slate)" stroke-width="1.2"/></svg>Free Clearovo Consultation</li>
      <li><svg class="tick" viewBox="0 0 12 12"><circle cx="6" cy="6" r="5" fill="none" stroke="var(--slate)" stroke-width="1.2"/><path d="M3.5 6.2 L5.3 8 L8.6 4.3" fill="none" stroke="var(--slate)" stroke-width="1.2"/></svg>New Patient Cleaning &amp; Exam</li>
      <li><svg class="tick" viewBox="0 0 12 12"><circle cx="6" cy="6" r="5" fill="none" stroke="var(--slate)" stroke-width="1.2"/><path d="M3.5 6.2 L5.3 8 L8.6 4.3" fill="none" stroke="var(--slate)" stroke-width="1.2"/></svg>$39 Emergency Exam &amp; X-rays</li>
    </ul>
    <p class="abs insurance">Most insurances accepted!</p>

    <div class="abs offer" style="left:38px;">
      <div class="tag">NEW PATIENT SPECIAL</div>
      <div class="lead">BUY ONE, GET ONE</div>
      <div class="big">FREE</div>
      <div class="body">Cleaning, Exam and X-Ray</div>
      <div class="fine">FOR $199<br><span style="font-size:9.5px">offer valid throughout 2017</span></div>
    </div>
    <div class="abs offer" style="left:241px;">
      <div class="tag">NEW PATIENT SPECIAL</div>
      <div class="lead">IMPLANT SPECIAL</div>
      <div class="big" style="margin-top:4px">$949</div>
      <div class="fine" style="margin-top:6px">Excluding graft if required<br>and final restoration</div>
    </div>
    <div class="abs offer" style="left:440px;">
      <div class="tag">NEW PATIENT SPECIAL</div>
      <div class="big" style="margin-top:10px">10%</div>
      <div class="fine" style="margin-top:6px">Senior, Military<br>Teacher and<br>Student Discount</div>
    </div>
    <div class="abs offer" style="left:639px;">
      <div class="tag">NEW PATIENT SPECIAL</div>
      <div class="big" style="margin-top:10px">15% <small>off</small></div>
      <div class="fine" style="margin-top:10px">Of any treatment for<br>loyal patients during 2017</div>
    </div>

    <div class="abs cta">
      <span>CALL TO MAKE AN APPOINTMENT</span>
      <svg viewBox="0 0 22 22"><circle cx="11" cy="11" r="10" fill="none" stroke="#fff" stroke-width="1.5"/><path d="M7.5 6.5 C7 9.5 10 14.5 14.5 15.5 L15.5 13.8 L13.4 12.6 L12.4 13.6 C11 13 9.4 11.3 8.8 9.8 L9.8 8.8 L8.8 6.6 Z" fill="#fff"/></svg>
      <span class="phone-num">801-555-0198</span>
    </div>
  </section>
</div>

<!-- Back of postcard -->
<div class="card-slot back">
  <section class="card back">
    <svg class="card-art" viewBox="0 0 850 550">
      <path d="M345 -6 C430 100 480 250 490 420" fill="none" stroke="var(--slate)" stroke-width="20"/>
      <path d="M368 -6 C455 110 500 250 505 400" fill="none" stroke="var(--lime)" stroke-width="6"/>
      <path d="M0 410 C250 370 560 440 850 440 V460 C560 470 250 420 0 450 Z" fill="#e9edf2"/>
      <path d="M0 440 C260 380 560 470 850 440 V470 C560 500 260 440 0 490 Z" fill="var(--lime)"/>
      <path d="M0 490 C260 440 560 500 850 442 V550 H0 Z" fill="var(--navy)"/>
    </svg>

    <div class="abs brand" style="left:28px; top:44px;">
      <span class="brand-dot"></span>
      <span class="brand-name">Tamblin Ridge Dental</span>
    </div>

    <div class="abs address-band">
      <svg width="12" height="16" viewBox="0 0 12 16"><path d="M6 0 C2.7 0 0 2.6 0 5.8 C0 10 6 16 6 16 C6 16 12 10 12 5.8 C12 2.6 9.3 0 6 0 Z" fill="#fff"/><circle cx="6" cy="5.8" r="2.2" fill="var(--slate)"/></svg>
      <span>4318 West Tamblin Road, Suite 260 Salt Lake City</span>
    </div>
    <div class="abs map-area" role="img" aria-label="Street map showing the clinic location near Ridgeline Drive"></div>

    <p class="abs directions">Located just off of Ridgeline Drive by the Valumart North<br>of Saffron Table</p>
    <p class="abs hours">OPEN MONDAY TO SATURDAY</p>
    <p class="abs insurance">Most insurances accepted!</p>

    <div class="abs badge"><span>FREE IMPLANT<br>AND CLEAROVO<br>CONSULTATIONS</span></div>

    <address class="abs return-address" style="font-style:normal">
      TAMBLIN RIDGE DENTAL<br>
      4318 West Tamblin Road, Suite 260<br>
      Salt Lake City, UT 84372<br>
      Phone: 801-555-0143<br>
      Fax: 801-555-0198
    </address>

    <div class="abs indicia">PRSRT STD<br>ECRWSS<br>U.S. POSTAGE<br><b>PAID</b><br>QPRS RETAIL</div>

    <div class="abs mail-block">
      <span class="route">*****************ECRWSS****</span>
      <p class="recipient">Local<br>Meridian Postal Customer</p>
    </div>

    <div class="abs cta" style="top:498px;">
      <span>CALL TO MAKE AN APPOINTMENT</span>
      <svg viewBox="0 0 22 22"><circle cx="11" cy="11" r="10" fill="none" stroke="#fff" stroke-width="1.5"/><path d="M7.5 6.5 C7 9.5 10 14.5 14.5 15.5 L15.5 13.8 L13.4 12.6 L12.4 13.6 C11 13 9.4 11.3 8.8 9.8 L9.8 8.8 L8.8 6.6 Z" fill="#fff"/></svg>
      <span class="phone-num">801-555-0198</span>
    </div>
  </section>
</div>

</body>
</html>
```